Eastlane Holdings Card

I would like a modern, eye catching card based off my logo design.
Info to include:
Tomas Velden (Card Name)
eastlaneholdings.com (Website)
555 283 6091 (Office/fax)
555 736 2840 (Business Cell)
tomas@eastlaneholdings.com (Work email)

Target Market(s)

Commercial real estate brokers, property owners.

Colors
ec1f27
757575

Requirements
Must have
• Name and info above. Not be lame!:)

```html
<!DOCTYPE html>
<html lang="en">
<head>
<meta charset="utf-8">
<title>Eastlane Holdings Card</title>
<link rel="stylesheet" href="https://fonts.googleapis.com/css2?family=Roboto+Condensed:wght@400;700&family=Roboto:wght@300;400&display=swap">
<style>
  :root {
    --brand-red: #a51d24;
    --accent-red: #c1272d;
    --ink-grey: #5f5f5f;
    --soft-grey: #757575;
    --rule-grey: #d6d6d6;
    --paper: #fbfbfb;
    --backdrop: #ececea;
    --white: #ffffff;
  }
  * { box-sizing: border-box; margin: 0; padding: 0; }
  html, body { width: 1200px; height: 911px; overflow: hidden; }
  body {
    background: var(--backdrop);
    font-family: "Roboto", Arial, sans-serif;
    position: relative;
  }
  .card {
    position: absolute;
    left: 280px;
    width: 640px;
    height: 366px;
    border-radius: 3px;
    box-shadow: 0 10px 24px rgba(0,0,0,0.18);
    overflow: hidden;
  }
  .card--front { top: 74px; background: var(--paper); border-bottom: 6px solid var(--brand-red); }
  .card--back { top: 472px; background: var(--brand-red); }

  .front__brand {
    position: absolute; left: 40px; top: 0; width: 260px; height: 100%;
    display: flex; align-items: center; justify-content: center; gap: 12px;
  }
  .brand-square { width: 22px; height: 22px; background: var(--accent-red); flex: none; }
  .brand-name {
    font-family: "Roboto Condensed", Arial, sans-serif;
    font-weight: 700; font-size: 27px; letter-spacing: 0.5px;
    color: var(--accent-red); text-transform: uppercase; white-space: nowrap;
  }
  .front__divider {
    position: absolute; left: 322px; top: 92px; width: 1px; height: 182px;
    background: var(--rule-grey);
  }
  .front__details { position: absolute; left: 356px; top: 92px; }
  .holder-name {
    font-family: "Roboto Condensed", Arial, sans-serif;
    font-weight: 700; font-size: 25px; color: var(--accent-red);
    text-transform: uppercase; letter-spacing: 0.3px; margin-bottom: 12px;
  }
  .address { font-size: 14px; line-height: 20px; color: var(--soft-grey); font-weight: 300; margin-bottom: 14px; }
  .contact-list { list-style: none; }
  .contact-list li {
    display: flex; align-items: center; gap: 10px;
    font-size: 14px; line-height: 22px; color: var(--ink-grey);
  }
  .contact-list svg { width: 12px; height: 12px; fill: var(--accent-red); flex: none; }

  .back__web {
    position: absolute; left: 34px; top: 50%;
    transform: translate(-50%, -50%) rotate(90deg);
    transform-origin: center; margin-left: 12px;
    color: var(--white); font-size: 13px; letter-spacing: 4px; white-space: nowrap; font-weight: 300;
  }
  .back__brand {
    position: absolute; inset: 0;
    display: flex; align-items: center; justify-content: center; gap: 16px;
  }
  .back__brand .brand-square { width: 30px; height: 30px; background: var(--white); }
  .back__brand .brand-name { color: var(--white); font-size: 38px; }
</style>
</head>
<body>
  <section class="card card--front" aria-label="Card front">
    <div class="front__brand">
      <span class="brand-square"></span>
      <span class="brand-name">Eastlane Holdings</span>
    </div>
    <div class="front__divider"></div>
    <div class="front__details">
      <h1 class="holder-name">Tomas Velden</h1>
      <p class="address">482 Alder Ridge court<br>Harlow MN 55012</p>
      <ul class="contact-list">
        <li><svg viewBox="0 0 12 12"><path d="M2.5 0.5 4.5 3 3.4 4.4c.7 1.6 2.1 3 3.7 3.7L8.5 7l2.5 2-1.2 2.2C5 11 1 7 .8 2.2z"/></svg>555 283 6091</li>
        <li><svg viewBox="0 0 12 12"><path d="M3 0h6a1 1 0 0 1 1 1v10a1 1 0 0 1-1 1H3a1 1 0 0 1-1-1V1a1 1 0 0 1 1-1zm.5 1.5v7.5h5V1.5z"/></svg>555 736 2840</li>
        <li><svg viewBox="0 0 12 12"><path d="M0 2h12v8H0zm1 1 5 3.5L11 3z"/></svg>tomas@eastlaneholdings.com</li>
        <li><svg viewBox="0 0 12 12"><circle cx="6" cy="6" r="6"/></svg>eastlaneholdings.com</li>
      </ul>
    </div>
  </section>

  <section class="card card--back" aria-label="Card back">
    <p class="back__web">www.eastlaneholdings.com</p>
    <div class="back__brand">
      <span class="brand-square"></span>
      <span class="brand-name">Eastlane Holdings</span>
    </div>
  </section>
</body>
</html>
```